Dr Selwyn aesthetics - Radiance Refined

I need a logo design for a new aesthetics business in London. I am specialised in Botox, Dermal Fillers & Skin Pigmentation treatment. The slogan is Radiance Refined. I would like some of the writing on the card to be embossed. I would like a very elegant design with the following detail:

1. White and gray scale background. For the font colour try gold OR silver shades.
2. The business involves working on the face mostly. Anything that can be done with letter 'M'? Or any other logo?
3. The front of the card should have Dr Selwyn Aesthetics and the slogan 'Radiance Refined'. The back should have my full name (Dr Selwyn Tarkett), qualifications (MBBS MSC BSC), my website (www.thebrindlecliniccollective.example), telephone number & email.
4. The back should also say treatments offered: ANTI-WRINKLE INJECTIONS. DERMAL FILLERS, LIP ENHANCEMENT, HYPERHYDROSIS. SKIN PIGMENTATION

Thank you very much
Updates

Project Deadline Extended
Reason: Delays in market research response. I would be grateful for an extension please. Many thanks

Target Market(s)

Female and male aged 18 and above

Industry/Entity Type

Business

Contact Information for Business Card

Elegant design. Square corners. British standard size. Horizontal design. Should contain the slogan, contact details.

Font styles to use
Script

Colors
c9c9c9
fbed22
ffffff
f5f5f5
000000

Requirements
Must have
• All that's mentioned above
Nice to have
• A logo with the outline of a female face. Or anything that can be done with the letter M of Selwyn.
Should not have
• No colours like green / purple / orange

```html
<!DOCTYPE html>
<html lang="en">
<head>
<meta charset="utf-8">
<title>Dr Selwyn Aesthetics – Business Card</title>
<link href="https://fonts.googleapis.com/css2?family=Great+Vibes&family=Open+Sans:wght@300;400;600&display=swap" rel="stylesheet">
<style>
  :root {
    --backdrop: #7d7d7d;
    --card-light: #ffffff;
    --card-dark: #000000;
    --gold: #c9a84a;
    --gold-soft: #d4b65a;
    --silver: #c9c9c9;
    --ghost: #262626;
  }
  * { margin: 0; padding: 0; box-sizing: border-box; }
  html, body {
    width: 1200px; height: 800px; overflow: hidden;
    background: var(--backdrop);
  }
  .canvas { position: relative; width: 1200px; height: 800px; }

  .card {
    position: absolute; top: 249px; width: 458px; height: 294px;
    overflow: hidden;
  }
  .card--front { left: 133px; background: var(--card-light); }
  .card--back { left: 623px; background: var(--card-dark); }

  /* Front */
  .brand-mark {
    position: absolute; left: 167px; top: 22px; width: 124px; height: 124px;
    border: 4px solid var(--gold); border-radius: 50%;
    display: flex; align-items: center; justify-content: center;
    font-family: "Great Vibes", cursive; font-size: 30px; color: var(--gold);
  }
  .brand-name {
    position: absolute; left: 0; right: 0; top: 170px; text-align: center;
    font-family: "Great Vibes", cursive; font-size: 41px; color: var(--gold);
    line-height: 1;
  }
  .brand-slogan {
    position: absolute; left: 0; right: 0; top: 224px; text-align: center;
    font-family: "Open Sans", sans-serif; font-weight: 300; font-size: 16px;
    letter-spacing: 3px; color: var(--silver);
  }

  /* Back */
  .ghost-ring {
    position: absolute; left: 212px; top: 8px; width: 290px; height: 290px;
    border: 8px solid var(--ghost); border-radius: 50%;
  }
  .holder-name {
    position: absolute; left: 35px; top: 56px;
    font-family: "Great Vibes", cursive; font-size: 35px; color: var(--gold);
    line-height: 1;
  }
  .credentials {
    position: absolute; left: 36px; top: 94px;
    font-family: "Open Sans", sans-serif; font-weight: 600; font-size: 11.5px;
    color: var(--gold-soft); letter-spacing: 0.3px;
  }
  .contact-list {
    position: absolute; left: 36px; top: 128px; list-style: none;
    font-family: "Open Sans", sans-serif; font-weight: 600; font-size: 12px;
    color: var(--gold-soft);
  }
  .contact-list li { display: flex; align-items: center; height: 16.5px; }
  .contact-list svg { width: 10px; height: 10px; margin-right: 7px; fill: var(--gold-soft); }
  .treatments {
    position: absolute; left: 0; width: 408px; top: 208px; text-align: center;
    font-family: "Open Sans", sans-serif; font-weight: 600; font-size: 11.5px;
    color: var(--gold-soft); line-height: 16px; letter-spacing: 0.2px;
  }
</style>
</head>
<body>
<main class="canvas">
  <section class="card card--front">
    <div class="brand-mark">Selwyn</div>
    <h1 class="brand-name">Dr Selwyn Aesthetics</h1>
    <p class="brand-slogan">Radiance Refined</p>
  </section>

  <section class="card card--back">
    <div class="ghost-ring"></div>
    <h2 class="holder-name">Dr Selwyn Tarkett</h2>
    <p class="credentials">MBBS MSC BSC</p>
    <ul class="contact-list">
      <li>
        <svg viewBox="0 0 10 10"><path d="M2 0.5 L3.6 2.6 L2.7 3.6 Q3.6 5.8 6.4 7.3 L7.4 6.4 L9.5 8 L8.4 9.5 Q4.5 9.3 0.6 1.6 Z"/></svg>
        (305) 555-0142
      </li>
      <li>
        <svg viewBox="0 0 10 10"><path d="M0.5 2 H9.5 V8.5 H0.5 Z M0.5 2 L5 5.5 L9.5 2" fill="none" stroke="currentColor"/><path d="M0.5 2 H9.5 L5 5.3 Z"/><rect x="0.5" y="2" width="9" height="6.5"/></svg>
        selwyn@thebrindlecliniccollective.example
      </li>
      <li>
        <svg viewBox="0 0 10 10"><circle cx="5" cy="5" r="4.6"/></svg>
        www.thebrindlecliniccollective.example
      </li>
    </ul>
    <p class="treatments">
      ANTI-WRINKLE INJECTIONS<br>
      DERMAL FILLERS, LIP ENHANCEMENT, HYPERHYDROSIS<br>
      SKIN PIGMENTATION
    </p>
  </section>
</main>
</body>
</html>
```